Redesign Company Website

Cellar Bridge new website: www.cellarbridge.example.com.au

Brief

• Cellar Bridge
Cellar Bridge is a relationship marketing company offering telesales services to partner wineries. We manage the winery’s database, engage in telesales campaigns and return great sales results to the winery.
Cellar Bridge currently operates in Australia, New Zealand and Canada, with plans to expand to the USA in 2014.

• The service
We take the winery’s database, clean it up, and typically run 2 telesales campaigns per year. The timing, products and pricing are agreed with the winery prior to the campaign.
There are multiple benefits for the winery: the database is engaged with the winery, sales conversions are high and the database is reliable and up to date.

• The size of the company
Cellar Bridge International employs about 20 people and plans to grow to 30. The turnover is in excess of AU$5m

• How long have you been established?
Cellar Bridge was rebranded 12 months ago, but the original entity has been trading for 10 years.

• The company in a few words
Dynamic
Responsive
Detailed
Bright
Independent
Friendly
Engaging

The old web site

www.cellarbridge.example.com.au

• What is good about the web site?
Clean look, succinct. No need to scroll down to get information.

• What don’t you like about the old web site?
Blocky top graphics look too cartoon-like
Stock photos
Dull, corporate look with no personality
Bad infographic on Services page
Limited contact information
Too much red

The new web site

• Outline the aims of the new web site
The main aim of the new website is to represent Cellar Bridge and its personality better. We hope to be able to engage wineries to come back to the site. It has to contain the relevant service and benefit information to convert new winery business.

• Who is the target audience?
This is above all a B2B website aimed at winery partners
It is not an e-commerce site, but we want wineries to come back frequently.

• How will your target audience be accessing your site
All forms, probably including mobile phones.

• What are the unique selling points for your company, your products or your services?
Independent
Reliable
Secure

• Competitors' web sites:
www.harvestcrewsample.com.au
http://www.morrowvaleestatesdirect.com.au/

The look and feel of the new web site

• Various web sites that we like the look & feel of.
http://www.tessbrook.com.au/ Great graphic on home page, good use of white space, uncluttered
http://pelvaquin.com/ Good use of space, clear navigation, bit quirky
http://www.casaremoli.com.au/ Ease of navigation, like the drop down “where we are” on the home page
http://www.starlanternrecaps.co.uk/ Great use of graphics for navigation etc.

• Logo and sample of corporate identity files attached.

Target Market(s)

Wineries in Australia, NZ, Canada, USA

Industry/Entity Type

E-Commerce

Requirements
Nice to have
• Would be good to have a blog on the site to create new content easily and frequently

```html
<!DOCTYPE html>
<html lang="en">
<head>
<meta charset="utf-8">
<title>Cellar Bridge – Benefits</title>
<link rel="stylesheet" href="https://fonts.googleapis.com/css2?family=Bebas+Neue&family=Didact+Gothic&family=Montserrat:wght@600;700;800&family=Arimo:wght@400;700&display=swap">
<style>
  :root {
    --red: #e21f26;
    --red-soft: #e8474c;
    --red-deep: #b01e24;
    --page: #f3f3f3;
    --ink: #222222;
    --grey: #8a8a8a;
    --grey-light: #9c9c9c;
    --body: #444444;
    --white: #ffffff;
    --bar: #1e1e1e;
  }
  * { margin: 0; padding: 0; box-sizing: border-box; }
  html, body { width: 1187px; height: 1200px; overflow: hidden; }
  body { position: relative; background: var(--page); font-family: "Arimo", Arial, sans-serif; color: var(--ink); }
  .abs { position: absolute; }

  /* Header */
  .site-header { position: absolute; left: 0; top: 0; width: 1187px; height: 176px; background: #f7f7f7; }
  .brand-name { left: 87px; top: 38px; font-family: "Montserrat", sans-serif; font-weight: 800; font-size: 56px; letter-spacing: -1.5px; color: var(--red); line-height: 1; }
  .intl-title { left: 609px; top: 34px; font-family: "Arimo", sans-serif; font-weight: 700; font-size: 25px; color: var(--red-soft); letter-spacing: 0.3px; }
  .intl-sub { left: 609px; top: 67px; font-weight: 700; font-size: 16px; color: var(--ink); letter-spacing: 0.2px; }
  .region-list { left: 609px; top: 114px; display: flex; list-style: none; font-weight: 700; font-size: 16px; color: var(--red-soft); }
  .region-list li { padding: 2px 0; }
  .region-list li + li { margin-left: 24px; padding-left: 24px; border-left: 3px solid var(--red-soft); }

  /* Navigation */
  .main-nav { position: absolute; left: 0; top: 176px; width: 1187px; height: 76px; background: var(--red-soft); border-top: 5px solid var(--red); }
  .nav-item { position: absolute; top: 17px; font-family: "Bebas Neue", sans-serif; font-size: 33px; color: var(--white); line-height: 1; }
  .nav-item.is-active { border-bottom: 3px solid var(--white); padding-bottom: 4px; }

  /* Benefits */
  .benefits-title { left: 239px; top: 301px; font-family: "Montserrat", sans-serif; font-weight: 700; font-size: 22px; letter-spacing: 1.6px; color: var(--red); }
  .benefits-kicker { left: 239px; top: 334px; font-family: "Arimo", sans-serif; font-weight: 700; font-size: 11px; color: var(--grey); letter-spacing: 0.3px; }
  .benefit { position: absolute; left: 239px; width: 700px; }
  .benefit-num { position: absolute; left: 0; top: -6px; font-family: "Montserrat", sans-serif; font-weight: 800; font-size: 30px; color: var(--ink); line-height: 1; }
  .benefit-title { margin-left: 22px; font-family: "Didact Gothic", sans-serif; font-size: 16.5px; color: var(--grey); line-height: 1.2; }
  .benefit-text { margin-left: 22px; margin-top: 3px; font-family: "Didact Gothic", sans-serif; font-size: 11px; color: var(--grey-light); line-height: 18px; }

  /* Database guarantee */
  .guarantee-bar { left: 214px; top: 708px; width: 734px; height: 18px; background: var(--bar); }
  .guarantee-lock { left: 236px; top: 650px; width: 94px; height: 110px; }
  .guarantee-note { left: 328px; top: 657px; font-family: "Didact Gothic", sans-serif; font-size: 16px; line-height: 19px; color: var(--grey); }
  .guarantee-head { left: 337px; top: 707px; font-family: "Montserrat", sans-serif; font-weight: 600; font-size: 15px; letter-spacing: 1.4px; color: var(--red); line-height: 20px; }
  .guarantee-sub { left: 339px; top: 728px; font-family: "Arimo", sans-serif; font-weight: 700; font-size: 14px; color: var(--red); }

  .intro-copy { left: 219px; top: 793px; width: 725px; font-size: 11px; line-height: 21px; color: var(--body); }

  /* Footer */
  .site-footer { position: absolute; left: 0; top: 919px; width: 1187px; height: 232px; background: var(--red-soft); border-top: 4px solid var(--red); }
  .contact-block { position: absolute; top: 48px; color: var(--white); }
  .contact-heading { font-weight: 700; font-size: 16px; margin-bottom: 20px; }
  .contact-line { font-size: 11.5px; line-height: 18.6px; }
  .footer-base { position: absolute; left: 0; top: 1151px; width: 1187px; height: 49px; background: var(--red-deep); color: var(--white); font-size: 11.5px; text-align: center; line-height: 49px; }
</style>
</head>
<body>

<header class="site-header">
  <div class="abs brand-name">cellarbridge</div>
  <div class="abs intl-title">CELLAR BRIDGE INTERNATIONAL</div>
  <div class="abs intl-sub">CONTACT YOUR LOCAL CELLAR BRIDGE REPRESENTATIVE TODAY</div>
  <ul class="abs region-list">
    <li>Australia</li>
    <li>New Zealand</li>
    <li>Hong Kong</li>
    <li>Canada</li>
  </ul>
</header>

<nav class="main-nav">
  <span class="nav-item" style="left:122px">Home</span>
  <span class="nav-item" style="left:258px">About Us</span>
  <span class="nav-item" style="left:428px">Services</span>
  <span class="nav-item is-active" style="left:596px">Benefits</span>
  <span class="nav-item" style="left:760px">Testimonials</span>
  <span class="nav-item" style="left:969px">Contact</span>
</nav>

<main>
  <h1 class="abs benefits-title">HOW A CELLAR BRIDGE CAMPAIGN CAN BENEFIT YOUR BRAND</h1>
  <p class="abs benefits-kicker">AT CELLAR BRIDGE, YOUR BRAND COMES FIRST - FIVE WAYS</p>

  <div class="benefit" style="top:363px">
    <span class="benefit-num">1</span>
    <h2 class="benefit-title">Sell more to people who already love your wine</h2>
    <p class="benefit-text">When a person takes the time to visit your cellar door, they create a strong connection with your brand and often become<br>the most active long term customers. Its the old 80/20 rule.</p>
  </div>
  <div class="benefit" style="top:431px">
    <span class="benefit-num">2</span>
    <h2 class="benefit-title">The results speak for themselves</h2>
    <p class="benefit-text">Such is the power of direct marketing: you can expect an increase in sales 5-10 times beyond regular snail and email with<br>your first campaign.</p>
  </div>
  <div class="benefit" style="top:499px">
    <span class="benefit-num">3</span>
    <h2 class="benefit-title">Every member has meaningful contact with the winery</h2>
    <p class="benefit-text">Even non-buyers come away with a strengthened relationship.</p>
  </div>
  <div class="benefit" style="top:548px">
    <span class="benefit-num">4</span>
    <h2 class="benefit-title">Quick sales turnover at a time that works for you</h2>
    <p class="benefit-text">We will co-ordinate campaigns to sync with your regular newsletter and email offers.</p>
  </div>
  <div class="benefit" style="top:599px">
    <span class="benefit-num">5</span>
    <h2 class="benefit-title">Up-to-date data returned to you from the campaign</h2>
    <p class="benefit-text">Contacting customers in this way allows you to better understand their needs.</p>
  </div>

  <div class="abs guarantee-bar"></div>
  <svg class="abs guarantee-lock" viewBox="0 0 94 110" aria-hidden="true">
    <path d="M22 48 V30 a25 25 0 0 1 50 0 V48" fill="none" stroke="#e21f26" stroke-width="11"/>
    <rect x="6" y="46" width="82" height="62" rx="9" fill="#e21f26"/>
    <rect x="14" y="54" width="66" height="46" rx="4" fill="#f3f3f3"/>
    <circle cx="47" cy="72" r="9" fill="#e21f26"/>
    <rect x="43" y="74" width="8" height="17" rx="2" fill="#e21f26"/>
  </svg>
  <p class="abs guarantee-note">Cellar Bridge will only ever sell your products to your members during agreed campaigns.<br>After all, they’re your members!</p>
  <p class="abs guarantee-head">WE GUARANTEE THE SECURITY OF YOUR DATABASE</p>
  <p class="abs guarantee-sub">This confidential data remains your legal property at all times.</p>

  <p class="abs intro-copy">Cellar Bridge provides a complete sales and marketing platform, from sales calls, Follow up contact and relationship building, our professional marketing team is capable of not only dazzling you and your members with our incredibly effective phone campaigns, but also providing presentations digital and printed campaigns, social media management &amp; consulting where required. Our sales team is renowned for being knowledgeable, articulate and passionate.</p>
</main>

<footer class="site-footer">
  <div class="contact-block" style="left:160px">
    <h3 class="contact-heading">Contact us – Australia:</h3>
    <p class="contact-line">Call 1800 555 013</p>
    <p class="contact-line">Email: info@cellarbridge.example.com.au</p>
    <p class="contact-line">Or drop in if you’re in town:</p>
    <p class="contact-line">42 Vintner Lane,</p>
    <p class="contact-line">Example Hills NSW 2999</p>
  </div>
  <div class="contact-block" style="left:500px">
    <h3 class="contact-heading">Contact us – Australia:</h3>
    <p class="contact-line">Call 1800 555 013</p>
    <p class="contact-line">Email: info@cellarbridge.example.com.au</p>
    <p class="contact-line">Or drop in if you’re in town:</p>
    <p class="contact-line">42 Vintner Lane,</p>
    <p class="contact-line">Example Hills NSW 2999</p>
  </div>
  <div class="contact-block" style="left:806px">
    <h3 class="contact-heading">Contact us – Australia:</h3>
    <p class="contact-line">Call 1800 555 013</p>
    <p class="contact-line">Email: info@cellarbridge.example.com.au</p>
    <p class="contact-line">Or drop in if you’re in town:</p>
    <p class="contact-line">42 Vintner Lane,</p>
    <p class="contact-line">Example Hills NSW 2999</p>
  </div>
</footer>
<div class="footer-base">© 2013 Cellar Bridge. All rights reserved.</div>

</body>
</html>
```